Upsell Vertical Banner Ad Design For B2B Marketing Agency Vertical 768px × 1180px IS THE SIZE

I need a banner made for my website www.brightlanepromotionhub.biz This banner will be an upsell advertisement for after someone signs up for my monthly program. When they login to their account for the 1st time I will give them the chance to upgrade their account to our annual program with just one click.

this is a page that upsells it currently to give you an idea how we market ourselves:
https://tlpx.pagevault-example.com/page/tlp-annual-upsell

Use this content:

Are You Ready To Commit To Taking Your Business To The Next Level?

Because We're In This For The Long-Haul and Dedicated To Your Success...

Save $300 By Upgrading To An Annual Membership And Pay Only $74/mth

((BUTTON))Yes, Upgrade My Plan Right Now!

*Must prepay the full year at only $898/yr!

Target Market(s)

business owners

Industry/Entity Type

Marketing

Requirements
Must have
• 768px × 1180px IS THE SIZE vertical

Use this content:

Nice to have
• Use this content:

Should not have
• Use this content:

```html
<!DOCTYPE html>
<html lang="en">
<head>
<meta charset="UTF-8">
<title>Annual Membership Upgrade</title>
<link href="https://fonts.googleapis.com/css2?family=Poppins:wght@400;500;600&display=swap" rel="stylesheet">
<style>
  :root {
    --brand-blue: #0b5aa5;
    --brand-blue-deep: #0a4f93;
    --white: #ffffff;
    --ink: #333333;
    --alert-red: #c4101c;
    --alert-red-dark: #8e0a12;
    --action-green: #4caf50;
    --photo-light: #e4e9ee;
    --photo-mid: #b9c3cc;
  }
  * { margin: 0; padding: 0; box-sizing: border-box; }
  html, body { width: 781px; height: 1200px; overflow: hidden; background: var(--white); }
  body { font-family: "Poppins", sans-serif; }
  .banner { position: relative; width: 781px; height: 1200px; overflow: hidden; background: var(--white); }

  .team-photo {
    position: absolute; left: 0; top: 270px; width: 781px; height: 358px;
    background: linear-gradient(180deg, var(--photo-light) 0%, var(--photo-mid) 55%, #d9dde1 100%);
  }

  .header-panel { position: absolute; left: 0; top: 0; width: 781px; height: 310px; }
  .headline {
    position: absolute; left: 0; top: 50px; width: 781px; text-align: center;
    color: var(--white); font-weight: 500; text-transform: uppercase;
  }
  .headline-top { display: block; font-size: 68px; line-height: 80px; letter-spacing: 0.5px; }
  .headline-mid {
    display: inline-block; margin: 3px 0 2px; padding: 0 14px;
    background: var(--white); color: var(--brand-blue);
    font-size: 27px; line-height: 39px; font-weight: 400;
  }
  .headline-bottom { display: block; font-size: 58px; line-height: 68px; letter-spacing: 0.5px; }

  .tagline-stroke { position: absolute; left: 20px; top: 625px; width: 752px; height: 96px; }
  .tagline {
    position: absolute; left: 0; top: 639px; width: 781px; text-align: center;
    color: var(--white); font-size: 22px; line-height: 34px; font-weight: 500;
  }

  .save-badge { position: absolute; left: 108px; top: 795px; width: 162px; height: 128px; }
  .save-badge-text {
    position: absolute; left: 150px; top: 806px; width: 110px; text-align: center;
    color: var(--white); font-weight: 600; font-size: 29px; line-height: 34px;
  }
  .offer {
    position: absolute; left: 296px; top: 794px;
    color: var(--ink); font-size: 25px; line-height: 32px; text-transform: uppercase;
  }
  .offer-price { color: var(--alert-red); }

  .footer-band { position: absolute; left: 0; top: 1010px; width: 781px; height: 190px; background: var(--brand-blue); }
  .cta-button {
    position: absolute; left: 162px; top: 959px; width: 455px; height: 90px;
    background: var(--action-green); border-radius: 6px 6px 14px 14px;
    box-shadow: 0 4px 8px rgba(0,0,0,0.25);
    color: var(--white); font-size: 21px; font-weight: 500;
    display: flex; align-items: center; justify-content: center;
  }
  .footnote {
    position: absolute; left: 0; top: 1090px; width: 781px; text-align: center;
    color: var(--white); font-size: 22px; line-height: 31px; font-weight: 500;
  }
</style>
</head>
<body>
<main class="banner">
  <div class="team-photo" role="img" aria-label="Photo of a business team gathered around a laptop at an office desk"></div>

  <svg class="header-panel" viewBox="0 0 781 310" aria-hidden="true">
    <path d="M0 0 H781 V270 Q781 288 764 289 L400 297 Q392 304 384 309 Q376 304 368 297 L16 283 Q0 282 0 266 Z" fill="var(--brand-blue)"/>
  </svg>
  <h1 class="headline">
    <span class="headline-top">Are You Ready</span>
    <span class="headline-mid">To Commit To Taking Your Business</span>
    <span class="headline-bottom">To The Next Level?</span>
  </h1>

  <svg class="tagline-stroke" viewBox="0 0 752 96" aria-hidden="true">
    <path d="M30 6 L740 0 L712 18 L748 30 L722 48 L744 62 L716 80 L730 92 L40 96 L52 84 L0 78 L36 62 L8 46 L44 30 L14 18 Z" fill="var(--brand-blue-deep)"/>
  </svg>
  <p class="tagline">Because We're In This For The Long-Haul and<br>Dedicated To Your Success...</p>

  <svg class="save-badge" viewBox="0 0 162 128" aria-hidden="true">
    <path d="M0 92 L56 128 L56 80 Z" fill="var(--alert-red-dark)"/>
    <path d="M30 0 H148 Q162 0 162 14 V76 Q162 90 148 90 H0 Z" fill="var(--alert-red)"/>
  </svg>
  <p class="save-badge-text">SAVE<br>$300</p>
  <p class="offer">By upgrading to an annual<br>membership and pay<br><span class="offer-price">Only $74/mth</span></p>

  <div class="footer-band"></div>
  <a class="cta-button">Yes, Upgrade My Plan Right Now!</a>
  <p class="footnote">Must prepay the full year<br>at only $898/yr!</p>
</main>
</body>
</html>
```